Need a business card design

Will be picking winner in 12 hours.
Need to use the logo (either one), and have place for only these four items. Color scheme is red/white/black.
-Name/Position
-Office/Mobile Phone Number
-Email
-Website

```html
<!DOCTYPE html>
<html lang="en">
<head>
<meta charset="utf-8">
<title>Halvek Global Security – Business Card</title>
<link href="https://fonts.googleapis.com/css2?family=Montserrat:wght@400;500;700&display=swap" rel="stylesheet">
<style>
  :root {
    --card-black: #1c1a1b;
    --brand-red: #c8202a;
    --text-white: #f2f2f2;
    --text-soft: #d9d9d9;
    --backdrop: #e6e3df;
  }
  * { box-sizing: border-box; margin: 0; padding: 0; }
  html, body {
    width: 1200px; height: 960px; overflow: hidden;
    background: var(--backdrop);
    font-family: "Montserrat", Arial, sans-serif;
  }
  .canvas { position: relative; width: 1200px; height: 960px; }
  .card {
    position: absolute;
    width: 560px; height: 320px;
    background: var(--card-black);
    border-radius: 6px;
    box-shadow: 0 10px 24px rgba(0,0,0,0.25);
    color: var(--text-white);
  }
  .card--front { left: 110px; top: 110px; }
  .card--back  { left: 530px; top: 520px; }

  .brand { display: flex; align-items: center; gap: 14px; }
  .brand__mark {
    width: 46px; height: 46px; border-radius: 50%;
    background: var(--brand-red); flex: none;
  }
  .brand__name {
    font-weight: 700; font-size: 18px; letter-spacing: 1.2px;
    color: var(--text-white); line-height: 1.2; text-transform: uppercase;
    white-space: nowrap;
  }
  .card--front .brand {
    position: absolute; left: 0; right: 0; top: 112px; justify-content: center;
  }
  .card--front .brand__mark { width: 64px; height: 64px; }
  .card--front .brand__name { font-size: 26px; letter-spacing: 1.5px; }
  .front__website {
    position: absolute; left: 0; right: 0; top: 222px;
    text-align: center; font-size: 15px; letter-spacing: 0.8px; color: var(--text-white);
  }

  .card--back .brand { position: absolute; left: 30px; top: 137px; }
  .back__divider {
    position: absolute; left: 322px; top: 60px; width: 1.5px; height: 200px;
    background: var(--brand-red);
  }
  .contact { position: absolute; left: 342px; top: 86px; right: 16px; }
  .contact__name {
    color: var(--brand-red); font-weight: 500; font-size: 20px;
    text-transform: uppercase; letter-spacing: 0.5px;
  }
  .contact__role { font-size: 13px; color: var(--text-soft); margin-top: 6px; }
  .contact__list { list-style: none; margin-top: 26px; font-size: 14px; }
  .contact__list li { display: flex; align-items: center; gap: 9px; line-height: 1.7; }
  .contact__icon { width: 12px; height: 12px; flex: none; }
  .contact__icon--solid { fill: var(--brand-red); }
  .contact__icon--line { fill: none; stroke: var(--brand-red); stroke-width: 2.5; }
</style>
</head>
<body>
<main class="canvas">
  <section class="card card--front" aria-label="Card front">
    <div class="brand">
      <span class="brand__mark"></span>
      <span class="brand__name">Halvek<br>Global Security</span>
    </div>
    <p class="front__website">www.halvekgs.com</p>
  </section>

  <section class="card card--back" aria-label="Card back">
    <div class="brand">
      <span class="brand__mark"></span>
      <span class="brand__name">Halvek<br>Global Security</span>
    </div>
    <div class="back__divider"></div>
    <div class="contact">
      <h1 class="contact__name">Daniel Orrin</h1>
      <p class="contact__role">General Manager</p>
      <ul class="contact__list">
        <li>
          <svg class="contact__icon contact__icon--solid" viewBox="0 0 24 24" aria-hidden="true"><path d="M6.6 10.8a15.1 15.1 0 0 0 6.6 6.6l2.2-2.2a1 1 0 0 1 1-.25 11.4 11.4 0 0 0 3.6.57 1 1 0 0 1 1 1V20a1 1 0 0 1-1 1A17 17 0 0 1 3 4a1 1 0 0 1 1-1h3.5a1 1 0 0 1 1 1c0 1.25.2 2.45.57 3.6a1 1 0 0 1-.25 1z"/></svg>
          +1 555 014 2287
        </li>
        <li>
          <svg class="contact__icon contact__icon--line" viewBox="0 0 24 24" aria-hidden="true"><rect x="2" y="5" width="20" height="14"/><path d="M2 5l10 8 10-8"/></svg>
          info@halvekgs.com
        </li>
        <li>
          <svg class="contact__icon contact__icon--line" viewBox="0 0 24 24" aria-hidden="true"><circle cx="12" cy="12" r="10"/><path d="M2 12h20M12 2c3 3 3 17 0 20M12 2c-3 3-3 17 0 20"/></svg>
          www.halvekgs.com
        </li>
      </ul>
    </div>
  </section>
</main>
</body>
</html>
```